I need a graphic for the promotion email for our "5th Yearly Crisis Preparedness Skills Camp" that incorporates our current logo and brand theme. I would like this graphic to funnel potentional attendees to register for a course. My perference would include a cool fire photo from our facility for the background. More information can be found on Marlowfieldcrew.com and also our Facebook.

```html
<!DOCTYPE html>
<html lang="en">
<head>
<meta charset="UTF-8">
<title>5th Yearly Crisis Preparedness Skills Camp – Marlowfield Crew</title>
<link rel="stylesheet" href="https://fonts.googleapis.com/css2?family=Orbitron:wght@800;900&family=Poppins:wght@400;500;700&display=swap">
<style>
  :root {
    --ink-dark: #0d0604;
    --ember-deep: #3a1407;
    --ember-mid: #8a3a12;
    --flame: #e07a2c;
    --flame-bright: #f5b46a;
    --brand-red: #e8402a;
    --button-orange: #e2541a;
    --text-light: #ffffff;
  }
  * { margin: 0; padding: 0; box-sizing: border-box; }
  html, body { width: 1200px; height: 600px; overflow: hidden; background: var(--ink-dark); }
  .banner {
    position: relative;
    width: 1200px;
    height: 600px;
    overflow: hidden;
    font-family: "Poppins", sans-serif;
    color: var(--text-light);
  }
  .banner__photo {
    position: absolute;
    inset: 0;
    background:
      radial-gradient(ellipse 320px 260px at 600px 90px, var(--flame-bright) 0%, var(--flame) 35%, transparent 75%),
      radial-gradient(ellipse 380px 200px at 720px 320px, rgba(224,122,44,0.75) 0%, transparent 75%),
      radial-gradient(ellipse 420px 220px at 1000px 480px, rgba(138,58,18,0.8) 0%, transparent 80%),
      linear-gradient(180deg, var(--ember-mid) 0%, var(--ember-deep) 60%, var(--ink-dark) 100%);
  }
  .banner__shade {
    position: absolute;
    inset: 0;
    background: linear-gradient(90deg, rgba(10,4,2,0.92) 0%, rgba(10,4,2,0.7) 30%, rgba(10,4,2,0.15) 60%, transparent 80%);
  }
  .brand {
    position: absolute;
    left: 62px;
    top: 92px;
    display: flex;
    align-items: center;
    gap: 18px;
  }
  .brand__dot {
    width: 46px;
    height: 46px;
    border-radius: 50%;
    background: var(--brand-red);
  }
  .brand__name {
    font-family: "Poppins", sans-serif;
    font-weight: 700;
    font-size: 30px;
    letter-spacing: 6px;
    text-transform: uppercase;
    color: var(--text-light);
  }
  .eyebrow {
    position: absolute;
    left: 60px;
    top: 181px;
    font-size: 22px;
    font-weight: 400;
    letter-spacing: 0.3px;
    text-transform: uppercase;
  }
  .headline {
    position: absolute;
    left: 60px;
    top: 228px;
    font-family: "Orbitron", sans-serif;
    font-weight: 900;
    font-size: 42px;
    line-height: 49px;
    text-transform: uppercase;
    letter-spacing: 0.5px;
  }
  .headline span { display: block; }
  .divider {
    position: absolute;
    left: 20px;
    top: 388px;
    width: 500px;
    height: 3px;
    background: linear-gradient(90deg, transparent 0%, var(--brand-red) 25%, var(--brand-red) 70%, transparent 100%);
  }
  .tagline {
    position: absolute;
    left: 65px;
    top: 403px;
    font-size: 19px;
    font-weight: 400;
    text-transform: uppercase;
  }
  .cta {
    position: absolute;
    left: 88px;
    top: 460px;
    width: 262px;
    height: 44px;
    border-radius: 22px;
    background: var(--button-orange);
    border: 2px solid rgba(255,255,255,0.75);
    box-shadow: 0 0 18px rgba(226,84,26,0.8);
    display: flex;
    align-items: center;
    justify-content: center;
    gap: 16px;
    font-weight: 700;
    font-size: 21px;
    color: var(--text-light);
    text-decoration: none;
    text-transform: uppercase;
  }
  .cta svg { width: 42px; height: 22px; }
</style>
</head>
<body>
  <div class="banner">
    <div class="banner__photo" role="img" aria-label="Night training photo: firefighters spraying water at a large industrial fire on a steel structure"></div>
    <div class="banner__shade"></div>

    <div class="brand">
      <span class="brand__dot"></span>
      <span class="brand__name">Marlowfield Crew</span>
    </div>

    <p class="eyebrow">Now open for registration</p>

    <h1 class="headline">
      <span>5th Yearly</span>
      <span>Crisis Preparedness</span>
      <span>Skills Camp</span>
    </h1>

    <div class="divider"></div>

    <p class="tagline">Hands-on industrial fire &amp; rescue training</p>

    <a class="cta" href="#register">
      Register now
      <svg viewBox="0 0 42 22" aria-hidden="true">
        <path d="M2 11 H38 M29 3 L38 11 L29 19" fill="none" stroke="#ffffff" stroke-width="3" stroke-linecap="round" stroke-linejoin="round"/>
      </svg>
    </a>
  </div>
</body>
</html>
```